Psychotherapy Website - Based in London

I am a newly trained psychotherapist and need a new website for www.rosalindfaber.co.uk.

I offer therapy for addiction, relationships, trauma and many other issues people face in their lives.

I want the website to be welcoming, gentle, feminine and for people to feel safe.

I do not like a page site that scrolls through sections, rather each page should be separate. Here some examples that i like. Sectional rather than scrolled.

https://www.hettiemarsh.com/
https://www.thequietwardrooms.com/

The imagery should be around pink using the flower in the logo / wording and around the site:

Here is a link to the flower for ideas:
https://www.pictofind.net/search?q=pink+gerbera&rlz=2D4KQTW_en-GBGB415GB415&source=lnms&tbm=isch&sa=X&ved=7cvQRtrk482h3PxZTuKLmeNBwXW_1AtXpVlKDbOQBmFLB&biw=1500&bih=889&dpr=2

RosalindFaber
Compassionate Psychotherapy

Is the logo and subheader for the website. Please use a typeface for the name that is appealing and professional.

Type face similar NOT EXLUSIVLY - JUST AN IDEA like this:
https://glowtonicstudio.com/

Basic business card i created as a rough idea below.

I have also added the website copy.

The headers are

Homepage
About Me
Therapy
Common Questions
Blog
Contact Me

Target Market(s)

Clients who are dealing with stress, trauma, pain, addiction

Industry/Entity Type

Therapy and Psychology

Coding

Coded - Design and coding required

Number of Pages Required

5+ page

Font styles to use
Serif
Sans Serif
Script

Colors
0054AA
0677BA
7BADD7
CADEEF
E8F1F8
0094D4
00A9DD
6FCCEA
C7EBF8
E9F6FB
E54698
E96AAD
F1A4CE
F9D9EA
FCEFF6

Requirements
Must have
• Pink Gerbera Flower integrated into design
Nice to have
• Images but not to stock imagery. Needs to look authentic and natural
Should not have
• Stock images of people. Images are important but needs to feel REAL

```html
<!DOCTYPE html>
<html lang="en">
<head>
<meta charset="utf-8">
<title>Rosalind Faber – Psychotherapy</title>
<link href="https://fonts.googleapis.com/css2?family=Poppins:ital,wght@0,300;0,400;0,500;0,600;1,300&family=Roboto+Slab:wght@600;700&family=Tinos&family=Great+Vibes&display=swap" rel="stylesheet">
<style>
:root{
  --pink:#e54698;
  --pink-2:#e96aad;
  --pink-3:#f1a4ce;
  --pink-4:#f9d9ea;
  --pink-5:#fcefF6;
  --ink:#1d1d1f;
  --text:#5b5b5f;
  --black:#151515;
  --white:#ffffff;
}
*{margin:0;padding:0;box-sizing:border-box}
html,body{width:1200px;height:5046px;overflow:hidden;background:var(--white)}
body{font-family:'Poppins',sans-serif;color:var(--text);position:relative}
.abs{position:absolute}
.serif{font-family:'Tinos',serif;color:var(--ink);font-weight:400}
.kicker{font-size:12.5px;color:var(--pink);text-transform:uppercase;letter-spacing:.3px}
.script{font-family:'Great Vibes',cursive}
.btn{position:absolute;background:var(--pink);color:#fff;border-radius:22px;font-size:14px;font-weight:500;text-transform:uppercase;display:flex;align-items:center;justify-content:center;letter-spacing:.3px}
.ph{position:absolute}

/* brand */
.brand{position:absolute;display:flex;align-items:center;gap:12px;color:#fff;font-family:'Poppins',sans-serif;font-weight:500;font-size:20px}
.brand-dot{width:30px;height:30px;border-radius:50%;background:var(--pink)}

/* hero */
.hero{position:absolute;left:0;top:0;width:1200px;height:720px;background:radial-gradient(circle at 870px 330px,#3a0f12 0 70px,#8a1236 71px 110px,#d3226e 150px,#e54698 280px,#b81b5e 420px,#6d0f35 640px,#3d1524 100%)}
.nav{position:absolute;top:42px;left:588px;display:flex;gap:24px;font-size:10.5px;color:#fff;text-transform:uppercase}
.nav .on{color:var(--pink-3);border-bottom:1px solid var(--pink-3);padding-bottom:4px}
.hero-title{position:absolute;left:118px;top:218px;font-family:'Roboto Slab',serif;font-weight:700;color:#fff;font-size:40px;line-height:49px;width:340px}
.hero-lead{position:absolute;left:120px;top:378px;width:360px;color:#fff;font-size:11px;line-height:19px;font-weight:300}
.social-dot{position:absolute;width:34px;height:34px;border-radius:50%;border:1.5px solid #fff}

/* about */
.blob{position:absolute;left:160px;top:860px;width:860px;height:560px;border-radius:48% 52% 40% 60%/55% 45% 55% 45%;background:radial-gradient(ellipse at center,#fde7f1 0,#fcf0f6 55%,rgba(252,239,246,0) 78%)}
.about-copy{position:absolute;left:513px;top:948px;width:410px;font-size:11.5px;line-height:19.5px;color:#505055}
.about-copy p{margin-bottom:10px}

/* therapy */
.card{position:absolute;top:1750px;width:232px;height:285px;overflow:hidden}
.card span{position:absolute;left:54px;bottom:20px;color:#fff;font-size:13px;text-transform:uppercase}
.card span:before{content:"";position:absolute;left:-34px;top:9px;width:22px;height:2px;background:var(--pink)}

/* faq */
.faq{position:absolute;left:107px;top:2995px;width:478px;height:410px;border:2px solid var(--pink-3)}
.faq h4{font-family:'Tinos',serif;font-weight:400;font-size:17px;color:var(--ink)}
.faq .row{position:absolute;left:20px;width:436px;border-top:1px solid #d9d9d9;padding-top:16px}

/* blog */
.post h3{font-family:'Tinos',serif;font-weight:400;font-size:18px;color:var(--ink)}
.post p{font-size:11px;line-height:19px;color:#77777b;margin-top:14px}
.post a{display:inline-block;margin-top:14px;font-size:11px;color:var(--pink);text-decoration:underline}

/* footer */
.foot h5{font-family:'Tinos',serif;font-weight:400;font-size:15px;color:var(--pink);text-transform:uppercase;letter-spacing:.5px}
.foot ul{list-style:none;margin-top:24px}
.foot li{font-size:11px;color:#e6e6e6;line-height:24px;padding-left:18px;position:relative}
.foot li:before{content:"";position:absolute;left:0;top:10px;width:5px;height:5px;border-radius:50%;background:var(--pink)}
.small{font-size:11px;color:#e6e6e6;line-height:18px}
.sq{position:absolute;width:90px;height:90px}
</style>
</head>
<body>

<!-- HERO -->
<section class="hero" role="img" aria-label="Close-up photograph of a vivid pink gerbera flower"></section>
<svg class="abs" style="left:0;top:560px" width="1200" height="170" viewBox="0 0 1200 170">
  <path fill="#fff" d="M0,92 L40,90 L70,104 L120,96 L170,110 L230,100 L280,112 L340,104 L380,118 L440,110 L500,124 L560,114 L610,130 L660,122 L700,138 L760,128 L810,146 L860,150 L900,140 L960,156 L1020,148 L1080,162 L1140,152 L1200,160 L1200,170 L0,170Z"/>
</svg>
<div class="brand" style="left:62px;top:32px"><span class="brand-dot"></span>Rosalind Faber</div>
<nav class="nav"><span class="on">Home</span><span>About Me</span><span>Theraphy</span><span>Common Questions</span><span>Blog</span></nav>
<div class="btn" style="left:998px;top:30px;width:140px;height:40px;font-weight:400;font-size:15px">Contact Me</div>
<div class="abs" style="left:74px;top:188px;color:#fff;font-size:14px">01</div>
<div class="abs" style="left:83px;top:215px;width:2px;height:255px;background:var(--pink)"></div>
<div class="abs" style="left:79px;top:468px;width:9px;height:9px;border-radius:50%;border:1.5px solid var(--pink)"></div>
<h1 class="hero-title">It's Time To See Yourself In a Diffrent Lights ?</h1>
<p class="hero-lead">I offer therapy for addiction, relationships, trauma and many other issues people face in their lives.</p>
<div class="btn" style="left:120px;top:433px;width:142px;height:40px">Contact Us</div>
<div class="social-dot" style="left:1104px;top:292px"></div>
<div class="social-dot" style="left:1104px;top:350px"></div>
<div class="social-dot" style="left:1104px;top:408px"></div>

<!-- ABOUT -->
<div class="kicker abs" style="left:0;width:1200px;text-align:center;top:738px">Welcome To</div>
<h2 class="serif abs" style="left:0;width:1200px;text-align:center;top:762px;font-size:32px;line-height:38px">TRAINEE<br>PSYCHOTHERAPIST</h2>
<div class="blob"></div>
<div class="ph" role="img" aria-label="Portrait photograph of the therapist" style="left:183px;top:910px;width:278px;height:278px;border-radius:50%;background:radial-gradient(circle at 50% 40%,#e9c9a8 0,#d9a98a 30%,#c65585 60%,#b3306a 100%)"></div>
<div class="script abs" style="left:240px;top:1206px;font-size:30px;color:#222">Rosalind Faber</div>
<div class="about-copy">
<p>Taking the first steps towards engaging in therapy can be a very personal journey.</p>
<p>Whilst, it can be challenging, I will ensure to make this journey as safe and as comfortable for you as possible.</p>
<p>Psychotherapy can help you see your current situation in new light, depth and clarity. It can change old and unhelpful perspectives and feelings about yourself and your life, and ultimately help you make positive changes. It might be the most important journey you'll ever make.</p>
<p>I provide a and non-judgmental space where any issues can be explored in complete confidentiality.</p>
<p>My practice is based in Richmond, where the room is homely, comfortable and welcoming. I believe a good environment contributes to great therapy.</p>
<p>Alternately, I am also available to provide therapy online, if this environment is more accommodating for my clients.</p>
<p>I am passionate about improving mental health and committed to offering therapy to all individuals regardless of their age, race, culture, disability, sexual orientation, or socio-economic background.</p>
</div>
<div class="ph" role="img" aria-label="Single pink gerbera flower on a green stem" style="left:975px;top:1150px;width:150px;height:200px;background:radial-gradient(circle at 70% 30%,#e54698 0,#ef6fae 30%,rgba(241,164,206,.5) 50%,rgba(255,255,255,0) 70%)"></div>

<!-- THERAPY -->
<div class="kicker abs" style="left:61px;top:1595px">We Are Experts In</div>
<h2 class="serif abs" style="left:61px;top:1618px;font-size:30px">OUR THERAPHY</h2>
<p class="abs" style="left:61px;top:1668px;width:470px;font-size:11px;line-height:19px">Therapy can help you to develop ways of coping better and overcoming issues you may feel are holding you back.</p>
<svg class="abs" style="left:1005px;top:1676px" width="140" height="36" viewBox="0 0 140 36">
  <line x1="0" y1="18" x2="80" y2="18" stroke="#e54698" stroke-width="1.5"/>
  <polyline points="100,6 90,18 100,30" fill="none" stroke="#e54698" stroke-width="2"/>
  <polyline points="124,6 134,18 124,30" fill="none" stroke="#222" stroke-width="2"/>
</svg>
<div class="card" style="left:0" role="img" aria-label="Photograph illustrating addiction"><div style="position:absolute;inset:0;background:linear-gradient(160deg,#d8d8d8,#6d6d6d 60%,#2b2b2b)"></div><span>Addiction</span></div>
<div class="card" style="left:247px" role="img" aria-label="Photograph illustrating anger"><div style="position:absolute;inset:0;background:linear-gradient(160deg,#eeeeee,#9a9a9a 55%,#474747)"></div><span>Anger</span></div>
<div class="card" style="left:495px" role="img" aria-label="Photograph illustrating anxiety"><div style="position:absolute;inset:0;background:linear-gradient(160deg,#cfcfcf,#7a6c66 55%,#3a3330)"></div><span>Anxiety</span></div>
<div class="card" style="left:742px" role="img" aria-label="Photograph illustrating emotional abuse"><div style="position:absolute;inset:0;background:linear-gradient(160deg,#5a5a5a,#bcbcbc 55%,#8b8b8b)"></div><span>Emotional Abuse</span></div>
<div class="card" style="left:990px;width:210px" role="img" aria-label="Photograph illustrating relationship issues"><div style="position:absolute;inset:0;background:linear-gradient(160deg,#e0e0e0,#8a7467 55%,#3a302a)"></div><span>Relationship</span></div>
<div class="btn" style="left:60px;top:2060px;width:150px;height:38px">Explore All</div>

<!-- TESTIMONIAL -->
<svg class="abs" style="left:0;top:2120px" width="1200" height="730" viewBox="0 0 1200 730" role="img" aria-label="Soft pink image of a woman with open arms in a field">
  <defs><linearGradient id="tg" x1="0" y1="0" x2="0" y2="1"><stop offset="0" stop-color="#e54698"/><stop offset=".55" stop-color="#e96aad"/><stop offset="1" stop-color="#d9468f"/></linearGradient></defs>
  <path fill="url(#tg)" d="M0,90 L60,84 L140,92 L220,80 L300,60 L360,30 L420,18 L520,24 L600,8 L700,20 L760,10 L820,40 L900,60 L980,70 L1060,90 L1140,100 L1200,96 L1200,620 L1150,660 L1100,700 L1020,690 L960,705 L900,680 L820,690 L760,670 L700,680 L640,660 L560,670 L500,640 L420,650 L340,630 L260,640 L180,620 L100,630 L0,610Z"/>
</svg>
<div class="ph" role="img" aria-label="Cluster of pink gerbera flowers" style="left:900px;top:2570px;width:300px;height:280px;background:radial-gradient(circle at 65% 45%,#f7c3dc 0,#ee6aa9 25%,rgba(229,70,152,.6) 45%,rgba(229,70,152,0) 70%)"></div>
<div class="abs" style="left:0;width:1200px;text-align:center;top:2220px;color:#fff;font-family:'Roboto Slab',serif;font-size:60px;line-height:60px">&ldquo;</div>
<h2 class="serif abs" style="left:0;width:1200px;text-align:center;top:2288px;font-size:30px;color:#fff">WHAT OUR CLIENT SAY ABOUT</h2>
<div class="script abs" style="left:0;width:1200px;text-align:center;top:2325px;font-size:26px;color:#222">Rosalind Faber</div>
<div class="ph" role="img" aria-label="Client portrait photograph" style="left:556px;top:2392px;width:90px;height:90px;border-radius:50%;border:3px solid #fff;background:radial-gradient(circle,#e8c4ae,#c98a74 60%,#9d5f52)"></div>
<svg class="abs" style="left:184px;top:2434px" width="20" height="34"><polyline points="16,2 4,17 16,32" fill="none" stroke="#fff" stroke-width="2"/></svg>
<svg class="abs" style="left:996px;top:2434px" width="20" height="34"><polyline points="4,2 16,17 4,32" fill="none" stroke="#fff" stroke-width="2"/></svg>
<p class="abs" style="left:290px;top:2508px;width:620px;text-align:center;color:#fff;font-size:13px;line-height:22px;font-style:italic;font-weight:300">" Lorem Ipsum has been the industry's standard dummy text ever since the, when an unknown printer took a galley of type and scrambled it to make a type specimen book. It has survived not only five centuries, but also the leap into electronic typesetting, remaining essentially unchanged. "</p>
<div class="abs" style="left:0;width:1200px;text-align:center;top:2630px;color:#fff;font-size:13px">&mdash;&nbsp;&nbsp;CLIENT NAME</div>

<!-- FAQ -->
<div class="kicker abs" style="left:107px;top:2897px">We Are Here For You</div>
<h2 class="serif abs" style="left:107px;top:2920px;font-size:30px">COMMON QUESTIONS</h2>
<div class="faq">
  <h4 class="abs" style="left:36px;top:26px;color:var(--pink)">How Long Will I Need Therapy For?</h4>
  <svg class="abs" style="left:420px;top:30px" width="18" height="12"><polyline points="1,1 9,10 17,1" fill="none" stroke="#e54698" stroke-width="1.6"/></svg>
  <div class="abs" style="left:36px;top:70px;width:400px;font-size:11px;line-height:19.5px;color:#77777b">
    <p>Therapy can last anywhere from one session to several months or even years. It all depends on what you want and need. Some people come to therapy with a very specific problem they need to solve and might find that one or two sessions is sufficient.</p>
    <p style="margin-top:12px">Other people come to therapy with more complicated issues they are grappling with and may feel they need a few months or more to understand and resolve their issues. Other people come with long-standing problems or difficult feelings and may benefit from longer-term therapy.</p>
  </div>
  <div class="row" style="top:300px"><h4>How Long Are The Sessions?</h4></div>
  <div class="row" style="top:354px"><h4>How Much Is Each Session?</h4></div>
  <svg class="abs" style="left:422px;top:320px" width="12" height="18"><polyline points="1,1 10,9 1,17" fill="none" stroke="#e54698" stroke-width="1.6"/></svg>
  <svg class="abs" style="left:422px;top:374px" width="12" height="18"><polyline points="1,1 10,9 1,17" fill="none" stroke="#e54698" stroke-width="1.6"/></svg>
</div>
<div class="abs" style="left:683px;top:3013px;width:374px;height:374px;border-radius:50%;border:3px solid var(--pink)"></div>
<div class="ph" role="img" aria-label="Hands with red nails holding a pale pink gerbera" style="left:700px;top:3030px;width:340px;height:340px;border-radius:50%;background:radial-gradient(circle at 50% 45%,#6a3a1e 0,#f4a6be 14%,#f5bccb 32%,#e5a596 55%,#c87366 80%,#9e5a55 100%)"></div>

<!-- SUBSCRIBE -->
<svg class="abs" style="left:0;top:3470px" width="1200" height="480" viewBox="0 0 1200 480" role="img" aria-label="Pink band with blurred gerbera petals">
  <defs><linearGradient id="sg" x1="0" y1="0" x2="0" y2="1"><stop offset="0" stop-color="#e96aad"/><stop offset="1" stop-color="#e54698"/></linearGradient></defs>
  <path fill="url(#sg)" d="M0,90 L80,80 L160,88 L240,70 L320,66 L400,40 L480,20 L560,8 L640,14 L720,6 L800,20 L880,44 L960,60 L1040,70 L1120,84 L1200,80 L1200,360 L1120,380 L1040,370 L960,390 L880,400 L800,420 L720,440 L640,460 L560,450 L480,430 L400,420 L320,400 L240,390 L160,380 L80,370 L0,380Z"/>
</svg>
<svg class="abs" style="left:568px;top:3578px" width="64" height="48" viewBox="0 0 64 48" fill="none" stroke="#fff" stroke-width="1.6">
  <rect x="2" y="10" width="42" height="30"/><polyline points="2,10 23,28 44,10"/><rect x="18" y="2" width="42" height="30"/><polyline points="18,2 39,20 60,2"/>
</svg>
<div class="abs" style="left:0;width:1200px;text-align:center;top:3656px;color:#fff;font-size:12px">SUBSCRIBE TO ALL ABOUT TRAINED PSYCHOTHERAPIST</div>
<h2 class="serif abs" style="left:0;width:1200px;text-align:center;top:3678px;font-size:30px;color:#fff">JOIN NOW FOR LATEST UPDATES</h2>
<div class="abs" style="left:336px;top:3752px;width:524px;height:38px;border-radius:20px;background:#fff;font-size:10px;color:#777;padding:12px 0 0 18px">Enter Email *</div>
<div class="btn" style="left:736px;top:3752px;width:126px;height:38px">Subscribe</div>

<!-- BLOG -->
<h2 class="serif abs" style="left:0;width:1200px;text-align:center;top:3998px;font-size:30px">BLOG POTS</h2>
<div class="ph" role="img" aria-label="Photograph of two people in a comforting embrace" style="left:172px;top:4075px;width:390px;height:210px;background:linear-gradient(120deg,#8b7a6c,#d8cbbd 45%,#a68f7c)"></div>
<div class="ph" role="img" aria-label="Photograph of a worried couple" style="left:593px;top:4075px;width:390px;height:210px;background:linear-gradient(120deg,#6c7a84,#c9b8a4 45%,#8a5b45)"></div>
<div class="post abs" style="left:172px;top:4305px;width:390px">
  <h3>Trauma And The Bears – a Fable</h3>
  <p>Once upon a time … there were humans on the savannah. It's a dangerous world. We need to find food, we need to protect ourselves from predators, we need shelter...</p>
  <a>Learn More</a> <span style="color:var(--pink);font-size:14px">&nbsp;&rarr;</span>
</div>
<div class="post abs" style="left:595px;top:4305px;width:390px">
  <h3>Why The Symptoms Of Trauma Make Sense</h3>
  <p>I looked again at the list of symptoms. It was long, and overwhelming, and ran to more than two pages. 'Signs you've been traumatised' promised the infographic.</p>
  <a>Learn More</a> <span style="color:var(--pink);font-size:14px">&nbsp;&rarr;</span>
</div>

<!-- FOOTER -->
<svg class="abs" style="left:0;top:4500px" width="1200" height="520" viewBox="0 0 1200 520">
  <path fill="#151515" d="M0,110 L70,100 L140,110 L220,96 L300,90 L380,100 L460,84 L540,70 L600,54 L640,30 L680,16 L720,28 L760,48 L820,60 L900,76 L980,84 L1060,96 L1140,100 L1200,96 L1200,520 L0,520Z"/>
</svg>
<div class="brand" style="left:62px;top:4672px;font-size:18px"><span class="brand-dot" style="width:26px;height:26px"></span>Rosalind Faber</div>
<svg class="abs" style="left:60px;top:4740px" width="16" height="22" viewBox="0 0 16 22"><path d="M8,1 C3,1 1,5 1,8 C1,13 8,21 8,21 C8,21 15,13 15,8 C15,5 13,1 8,1Z" fill="none" stroke="#e54698" stroke-width="1.6"/><circle cx="8" cy="8" r="2.5" fill="#e54698"/></svg>
<div class="abs small" style="left:90px;top:4735px;width:210px">Address:<br>Linden Community Hall 27 Marlow Road East Twickenham TW1 4QZ</div>
<svg class="abs" style="left:60px;top:4808px" width="18" height="18" viewBox="0 0 18 18"><path d="M4,1 L7,5 L5,7 C6,10 8,12 11,13 L13,11 L17,14 L15,17 C8,17 1,10 1,3Z" fill="none" stroke="#e54698" stroke-width="1.6"/></svg>
<div class="abs" style="left:90px;top:4806px;color:#fff;font-size:15px">07700 900418</div>
<svg class="abs" style="left:60px;top:4846px" width="20" height="14" viewBox="0 0 20 14"><rect x="1" y="1" width="18" height="12" fill="none" stroke="#e54698" stroke-width="1.6"/><polyline points="1,1 10,8 19,1" fill="none" stroke="#e54698" stroke-width="1.6"/></svg>
<div class="abs small" style="left:90px;top:4844px">rosalindfaber@quietcounsel.co.uk</div>
<div class="abs" style="left:62px;top:4884px;width:34px;height:34px;border-radius:50%;background:var(--pink)"></div>
<div class="abs" style="left:104px;top:4884px;width:34px;height:34px;border-radius:50%;background:var(--pink)"></div>
<div class="abs" style="left:146px;top:4884px;width:34px;height:34px;border-radius:50%;background:var(--pink)"></div>

<div class="foot abs" style="left:330px;top:4648px"><h5>Sitemap</h5>
<ul><li>Home</li><li>About Me</li><li>Theraphy</li><li>Common Questions</li><li>Blog</li><li>Contact Me</li></ul></div>
<div class="foot abs" style="left:562px;top:4648px"><h5>Your Journey</h5>
<ul><li>Addiction</li><li>Relationships</li><li>Trauma</li><li>HIV</li><li>LGTB Issues</li><li>Sexual Abuse</li><li>Negative thinking</li><li>Self Sabotage</li><li>Depression</li><li>Pschosis</li><li style="color:var(--pink);text-decoration:underline">View All</li></ul></div>
<div class="foot abs" style="left:818px;top:4648px"><h5>Follow Us On</h5></div>
<div class="sq" role="img" aria-label="Gallery photo" style="left:818px;top:4690px;background:linear-gradient(135deg,#7a5aa0,#e0c6d6)"></div>
<div class="sq" role="img" aria-label="Gallery photo" style="left:916px;top:4690px;background:linear-gradient(135deg,#d6e3c8,#8a6a52)"></div>
<div class="sq" role="img" aria-label="Gallery photo" style="left:1014px;top:4690px;background:linear-gradient(135deg,#c98a3c,#5b3a20)"></div>
<div class="sq" role="img" aria-label="Gallery photo" style="left:818px;top:4788px;background:linear-gradient(135deg,#6b4a3c,#b48a74)"></div>
<div class="sq" role="img" aria-label="Gallery photo" style="left:916px;top:4788px;background:linear-gradient(135deg,#4a3a38,#c9a48a)"></div>
<div class="sq" role="img" aria-label="Gallery photo of pink gerberas" style="left:1014px;top:4788px;background:radial-gradient(circle,#f1a4ce,#e54698 60%,#a82a6a)"></div>
<div class="abs" style="left:818px;top:4905px;width:286px;text-align:center;font-size:11px;color:var(--pink);font-style:italic;text-decoration:underline">#Rosalind Faber</div>

<div class="abs" style="left:0;top:5012px;width:1200px;height:34px;background:var(--pink);color:#fff;font-size:10px;text-align:center;line-height:34px">©TRAINEE PSYCHOTHERAPIST - 2021 All rights reserved.</div>

</body>
</html>
```